Corvell Advisory

Business Development Consulting Firm

Target Market(s)

Federal Government, 8(a) companies, Small Businesses

Industry/Entity Type

Private Sector, US Government

Contact Information for Business Card

8(a) Program Capture, Business Development, Industry Trends & Analysis, Strategic Teaming, Cyber Solutions

Colors

Designer to choose colors to be used in the design.

```html
<!DOCTYPE html>
<html lang="en">
<head>
<meta charset="utf-8">
<title>Corvell Advisory — Business Card</title>
<link href="https://fonts.googleapis.com/css2?family=Source+Sans+3:wght@400;600;700&display=swap" rel="stylesheet">
<style>
  :root {
    --page: #efefef;
    --card: #1f1612;
    --gold: #f2c04a;
    --ink-light: #f4efe9;
    --icon-ink: #1f1612;
  }
  * { box-sizing: border-box; margin: 0; padding: 0; }
  html, body { width: 1200px; height: 1200px; overflow: hidden; }
  body {
    background: var(--page);
    font-family: "Source Sans 3", "Source Sans Pro", sans-serif;
    position: relative;
  }
  .card {
    position: absolute;
    left: 262px;
    width: 674px;
    height: 374px;
    background: var(--card);
    border-radius: 7px;
  }
  .card--front { top: 184px; }
  .card--back { top: 626px; }

  /* Front */
  .brand-mark {
    position: absolute;
    border-radius: 50%;
    background: var(--gold);
  }
  .card--front .brand-mark { left: 148px; top: 132px; width: 108px; height: 108px; }
  .brand-name {
    position: absolute;
    color: var(--gold);
    font-weight: 700;
    font-variant: small-caps;
    line-height: 1;
  }
  .card--front .brand-name {
    left: 300px; top: 136px;
    font-size: 56px;
    letter-spacing: 1px;
  }
  .brand-name span { display: block; }
  .card--front .brand-name span + span { margin-top: 2px; }

  /* Back */
  .card--back .brand-mark { left: 102px; top: 46px; width: 48px; height: 48px; }
  .card--back .brand-name {
    left: 102px; top: 104px;
    font-size: 17px;
    letter-spacing: 0.5px;
  }
  .contact-list {
    position: absolute;
    left: 108px; top: 164px;
    list-style: none;
  }
  .contact-item {
    display: flex;
    align-items: center;
    height: 32px;
    margin-bottom: 8.5px;
    color: var(--ink-light);
    font-size: 12px;
    font-variant: small-caps;
    letter-spacing: 0.3px;
  }
  .contact-item:first-child { font-variant: normal; font-size: 12px; }
  .contact-icon {
    width: 32px; height: 32px;
    border-radius: 50%;
    background: var(--gold);
    display: flex; align-items: center; justify-content: center;
    margin-right: 17px;
    flex-shrink: 0;
  }
  .contact-icon svg { width: 18px; height: 18px; }
  .person {
    position: absolute;
    right: 64px; top: 90px;
    text-align: right;
    color: var(--ink-light);
  }
  .person-name {
    font-size: 26px;
    font-weight: 600;
    font-variant: small-caps;
    letter-spacing: 1px;
    line-height: 1;
  }
  .services {
    list-style: none;
    margin-top: 52px;
    font-size: 17px;
    font-weight: 600;
    font-variant: small-caps;
    letter-spacing: 0.4px;
    line-height: 24.7px;
  }
</style>
</head>
<body>
  <section class="card card--front" aria-label="Card front">
    <div class="brand-mark"></div>
    <div class="brand-name"><span>Corvell</span><span>Advisory</span></div>
  </section>

  <section class="card card--back" aria-label="Card back">
    <div class="brand-mark"></div>
    <div class="brand-name">Corvell Advisory</div>

    <ul class="contact-list">
      <li class="contact-item">
        <span class="contact-icon">
          <svg viewBox="0 0 24 24" fill="var(--icon-ink)"><path d="M6.6 10.8a15.1 15.1 0 0 0 6.6 6.6l2.2-2.2a1 1 0 0 1 1-.25 11.4 11.4 0 0 0 3.6.57 1 1 0 0 1 1 1V20a1 1 0 0 1-1 1A17 17 0 0 1 3 4a1 1 0 0 1 1-1h3.5a1 1 0 0 1 1 1c0 1.25.2 2.45.57 3.57a1 1 0 0 1-.25 1z"/></svg>
        </span>
        000 000 000
      </li>
      <li class="contact-item">
        <span class="contact-icon">
          <svg viewBox="0 0 24 24" fill="var(--icon-ink)"><path d="M3 6h18v12H3z" opacity="0"/><path d="M3 7.5 12 13l9-5.5V18H3z"/><path d="M3 6h18l-9 5.5z"/></svg>
        </span>
        mailaddress@mail.com
      </li>
      <li class="contact-item">
        <span class="contact-icon">
          <svg viewBox="0 0 24 24" fill="none" stroke="var(--icon-ink)" stroke-width="2"><circle cx="12" cy="12" r="9"/><path d="M3 12h18M12 3c3 3 3 15 0 18M12 3c-3 3-3 15 0 18"/></svg>
        </span>
        www.website.com
      </li>
      <li class="contact-item">
        <span class="contact-icon">
          <svg viewBox="0 0 24 24" fill="none" stroke="var(--icon-ink)" stroke-width="2"><path d="M12 21s-6-6.2-6-11a6 6 0 0 1 12 0c0 4.8-6 11-6 11z"/><circle cx="12" cy="10" r="2.2"/></svg>
        </span>
        Location
      </li>
    </ul>

    <div class="person">
      <h1 class="person-name">John Doe</h1>
      <ul class="services">
        <li>Program Capture</li>
        <li>Business Development</li>
        <li>Industry Trends &amp; Analysis</li>
        <li>Strategic Teaming</li>
      </ul>
    </div>
  </section>
</body>
</html>
```